We are looking for a new PowerPoint template for our new CI

Hey pixelfair! For 25 years we have been an owner-managed IT system house with tradition, values and a great team. After more than 10 years, we would like to upgrade our company and design the entire CI contemporary and modern. Therefore we are looking for a Powerpoint Template which fits to our logo, the colors and an IT company. Details about our company and our service portfolio can be found on our homepage. We are currently adapting our homepage to the new CI resulting from the logo revision. Homepage: http://stage.netvora-example.de Color codes: Gray = RGB: 4040404040 White = RGB: F5F5F5F5F5 Orange = RGB: F7931E Our slogan: We keep your system running Our address data: Company = NV Kelmar GmbH Street = Lindenpfad 8 POSTCODE = 48261 City = Hollbrunn We look forward to your ideas and thank you all in advance.

Target Market(s)

Our target group are companies with 10 to 100 employees from all industrial sectors, eg https://www.ormitz-holzbau-example.de/ https://www.kravel-logistik-example.de/ https://www.finsau-example.de/ de /

Colors

Designer to choose colors to be used in the design.

Requirements
Must have
• We are looking for a modern IT design in gray / orange. The basis of the design should be our logo. The template should have two different layouts and three different layouts for content. Our logo and slogan should be clearly visible on the start layout. In addition, an area should be reserved for the name of a speaker and the occasion of the presentation.

```html
<!DOCTYPE html>
<html lang="de">
<head>
<meta charset="utf-8">
<title>NV Kelmar – Präsentationsvorlage</title>
<link href="https://fonts.googleapis.com/css2?family=Open+Sans:ital,wght@0,300;0,400;0,600;0,700;1,400&display=swap" rel="stylesheet">
<style>
:root{
  --orange:#f7931e;
  --orange-soft:#f9a845;
  --gray:#404040;
  --gray-mid:#5a5a5a;
  --white:#ffffff;
  --paper:#f5f5f5;
  --rule:#e0b04a;
  --text:#3a3a3a;
}
*{margin:0;padding:0;box-sizing:border-box}
html,body{width:1200px;height:1057px;overflow:hidden;background:var(--white);font-family:"Open Sans",sans-serif;color:var(--text)}
.board{position:relative;width:1200px;height:1057px}
.slide{position:absolute;width:640px;height:360px;background:var(--white);transform:scale(.5875);transform-origin:0 0;box-shadow:0 2px 10px rgba(0,0,0,.35);overflow:hidden}
.abs{position:absolute}
.corner{position:absolute;left:32px;top:36px;width:18px;height:18px}
.title{position:absolute;left:50px;top:34px;font-size:28px;font-weight:400;color:var(--gray);white-space:nowrap}
.footer-rule{position:absolute;height:1px;background:var(--rule)}
.footer-url{position:absolute;font-size:8px;color:var(--gray)}
.tile{position:absolute;width:160px;height:120px;background:var(--orange-soft);display:flex;align-items:center;justify-content:center;text-align:center;font-size:12px;color:var(--gray);padding:10px;line-height:1.2}
.photo{position:absolute}
.bullets{position:absolute;list-style:none;font-size:9px;color:var(--gray)}
.bullets li{position:relative;padding-left:14px;margin-bottom:11px;line-height:1.2}
.bullets li::before{content:"•";position:absolute;left:0}
.note-box{position:absolute;background:var(--orange);color:var(--white);font-size:11px;line-height:1.2;display:flex;align-items:center;padding:0 16px}
.pillar{position:absolute;top:140px;width:178px;height:162px;text-align:center;padding:30px 12px 0}
.pillar h3{font-weight:400;font-size:13px;margin-bottom:14px}
.pillar p{font-size:8px;line-height:1.25}
.pillar-gray{background:var(--gray-mid)}
.pillar-gray h3,.pillar-gray p{color:var(--orange)}
.pillar-orange{background:var(--orange)}
.pillar-orange h3,.pillar-orange p{color:var(--white)}
.icon-box{position:absolute;top:110px;width:58px;height:58px;display:flex;align-items:center;justify-content:center}
.price-col{position:absolute;top:108px;width:171px;height:188px;background:var(--orange-soft)}
.price-head{height:44px;background:var(--gray);color:var(--white);font-size:11px;display:flex;align-items:center;justify-content:center}
.price-col p{font-size:8px;text-align:center;color:var(--gray);padding:14px 14px 0;line-height:1.2;height:98px}
.price-pill{margin:0 auto;width:96px;height:32px;background:var(--gray);border-radius:4px;color:var(--white);font-size:22px;display:flex;align-items:center;justify-content:center;font-weight:300}
.price-pill sup{font-size:12px;margin-left:4px}
.stat{position:absolute;top:230px;width:80px;text-align:center}
.stat-badge{position:relative;margin:0 auto;width:52px;height:38px;background:var(--orange);color:var(--white);font-size:18px;display:flex;align-items:center;justify-content:center}
.stat-badge::after{content:"";position:absolute;bottom:-8px;left:50%;margin-left:-8px;border:8px solid transparent;border-bottom:0;border-top-color:var(--orange)}
.stat span{display:block;margin-top:16px;font-size:8px;color:var(--gray)}
</style>
</head>
<body>
<div class="board">

<section class="slide" style="left:16px;top:39px;background:linear-gradient(90deg,#f4f4f6 0%,#eceef2 100%)">
  <div class="photo" role="img" aria-label="Person working on a laptop, seen from above, with faint technology icons" style="left:230px;top:0;width:410px;height:360px;background:linear-gradient(135deg,#f1f2f5 0%,#d9dce3 50%,#e8eaee 100%)"></div>
  <div class="abs" style="left:32px;top:150px;display:flex;align-items:center;gap:10px">
    <span style="width:22px;height:22px;background:var(--orange);display:block"></span>
    <span style="font-size:38px;font-weight:700;color:var(--gray);letter-spacing:1px">NV Kelmar</span>
  </div>
  <div class="abs" style="left:36px;top:220px;font-size:14px;font-style:italic;color:var(--orange)">We keep your system running...</div>
  <div class="abs" style="left:36px;top:264px;font-size:9px;color:var(--orange);line-height:1.8">Presented by : XXXXXXX<br>www.stage.netvora-example.de</div>
  <div class="abs" style="left:147px;top:340px;font-size:8px;color:var(--gray)">Seit über 25 Jahren ein inhabergeführtes Familienunternehmen auf der Kelmtaler Höhe</div>
</section>

<section class="slide" style="left:414px;top:39px">
  <svg class="corner" viewBox="0 0 18 18"><polygon points="0,0 18,0 0,18" fill="#f7931e"/></svg>
  <h2 class="title">About Us</h2>
  <div class="pillar pillar-gray" style="left:60px"><h3>IT Systemhaus</h3><p>Drei Säulen bilden die Basis für die Zufriedenheit unserer Kunden. Die individuelle IT-Beratung, perfekte IT-Lösungen für jeden Anspruch im Bereich Hard- und Software sowie IT-Service der über eine reine Systemwartung weit hinausgeht.</p></div>
  <div class="pillar pillar-orange" style="left:238px"><h3>Softwareschmiede</h3><p>Arbeitsschutz Management Software aus der Praxis für die Praxis. Ihre Vorgesetzten, Fachkräfte für Arbeitssicherheit, Administratoren und Kontrollorgane werden durch NV Kelmar unterstützt und entlastet.</p></div>
  <div class="pillar pillar-gray" style="left:416px"><h3>Projektmanagement</h3><p>Vom ersten Entwurf bis zur Umsetzung unterstützen wir Sie gerne bei Ihren IT Projekten. Mit unserer langjährigen Erfahrung kennen wir bestens die "Go's" und "No-Go's". Ihr Erfolg ist auch unser Erfolg!</p></div>
  <div class="icon-box" style="left:120px;background:var(--orange)"><svg width="34" height="30" viewBox="0 0 34 30" fill="none" stroke="#404040" stroke-width="1.6"><circle cx="14" cy="9" r="6"/><path d="M3 28c0-7 5-11 11-11s11 4 11 11"/><path d="M20 4a6 6 0 0 1 0 11M25 18c4 2 6 5 6 10"/></svg></div>
  <div class="icon-box" style="left:298px;background:var(--gray-mid)"><svg width="34" height="30" viewBox="0 0 34 30" fill="none" stroke="#f7931e" stroke-width="1.8"><path d="M12 4 2 15l10 11M22 4l10 11-10 11"/></svg></div>
  <div class="icon-box" style="left:476px;background:var(--orange)"><svg width="32" height="32" viewBox="0 0 32 32" fill="none" stroke="#404040" stroke-width="1.6"><path d="M2 30h28M8 30v-6h6v-6h6v-6h6v18M10 16 24 3M17 3h7v7"/></svg></div>
  <div class="footer-rule" style="left:155px;top:336px;width:240px"></div>
  <div class="footer-url" style="left:408px;top:330px">www.stage.netvora-example.de</div>
</section>

<section class="slide" style="left:812px;top:39px">
  <svg class="corner" viewBox="0 0 18 18"><polygon points="0,0 18,0 0,18" fill="#f7931e"/></svg>
  <h2 class="title" style="left:42px">OUR PORTFOLIO</h2>
  <div class="photo" role="img" aria-label="Technician repairing a computer mainboard" style="left:30px;top:87px;width:188px;height:120px;background:linear-gradient(135deg,#3a5a8a,#c9cdd3)"></div>
  <div class="tile" style="left:45px;top:187px;height:121px">Hardware und Software</div>
  <div class="tile" style="left:242px;top:103px;height:121px">IT Management</div>
  <div class="photo" role="img" aria-label="Monitoring dashboard screenshot with charts" style="left:226px;top:225px;width:180px;height:100px;background:linear-gradient(180deg,#f7f7f7,#e9ecef)"></div>
  <div class="photo" role="img" aria-label="Two businessmen discussing documents" style="left:420px;top:87px;width:188px;height:120px;background:linear-gradient(135deg,#dfe2e6,#a9b0b8)"></div>
  <div class="tile" style="left:438px;top:187px;height:121px">Projektmanagement</div>
  <div class="footer-rule" style="left:32px;top:336px;width:450px"></div>
  <div class="footer-url" style="left:492px;top:330px">www.stage.netvora-example.de</div>
</section>

<section class="slide" style="left:16px;top:296px">
  <svg class="corner" viewBox="0 0 18 18"><polygon points="0,0 18,0 0,18" fill="#f7931e"/></svg>
  <h2 class="title" style="left:42px">OUR PORTFOLIO</h2>
  <div class="tile" style="left:44px;top:92px;align-items:flex-start;padding-top:44px">Corvana - Die Praxissoftware</div>
  <div class="photo" role="img" aria-label="Practice software advertisement with a woman holding a tablet" style="left:40px;top:200px;width:168px;height:122px;background:linear-gradient(135deg,#f3a23b,#e98a17)"></div>
  <div class="photo" role="img" aria-label="Illuminated server rack in a data centre" style="left:231px;top:92px;width:188px;height:95px;background:linear-gradient(135deg,#143d5c,#2fb8d8)"></div>
  <div class="tile" style="left:245px;top:198px">NV Kelmar - Managed Backup</div>
  <div class="tile" style="left:437px;top:92px">Hochleistungs Firewalls und VPN</div>
  <div class="photo" role="img" aria-label="Stack of red firewall appliances" style="left:424px;top:205px;width:188px;height:118px;background:linear-gradient(180deg,#f2f2f2,#d8272d)"></div>
  <div class="footer-rule" style="left:32px;top:336px;width:450px"></div>
  <div class="footer-url" style="left:492px;top:330px">www.stage.netvora-example.de</div>
</section>

<section class="slide" style="left:414px;top:296px">
  <svg class="corner" viewBox="0 0 18 18"><polygon points="0,0 18,0 0,18" fill="#f7931e"/></svg>
  <h2 class="title" style="left:42px">OUR PORTFOLIO</h2>
  <div class="photo" role="img" aria-label="Telephone system web interface screenshot" style="left:33px;top:92px;width:180px;height:95px;background:linear-gradient(180deg,#2f5d9a 0 6px,#f5f6f8 6px)"></div>
  <div class="tile" style="left:44px;top:188px">Virtuelle Telefonanlage und VoIP Telefonie</div>
  <div class="tile" style="left:242px;top:104px">Hotline und Support</div>
  <div class="photo" role="img" aria-label="Support agent with headset at a computer" style="left:228px;top:220px;width:180px;height:105px;background:linear-gradient(135deg,#d7dde3,#8a9aa8)"></div>
  <div class="photo" role="img" aria-label="Network switch with many cables" style="left:422px;top:87px;width:180px;height:120px;background:linear-gradient(135deg,#1f2b3a,#7f96b0)"></div>
  <div class="tile" style="left:437px;top:205px;height:103px">Service vor Ort</div>
  <div class="footer-rule" style="left:32px;top:336px;width:450px"></div>
  <div class="footer-url" style="left:492px;top:330px">www.stage.netvora-example.de</div>
</section>

<section class="slide" style="left:812px;top:296px">
  <svg class="corner" viewBox="0 0 18 18"><polygon points="0,0 18,0 0,18" fill="#f7931e"/></svg>
  <h2 class="title">Professionelles IT Management</h2>
  <div class="photo" role="img" aria-label="Desktop monitor showing a monitoring dashboard" style="left:35px;top:118px;width:165px;height:175px;background:linear-gradient(180deg,#2b2b2b 0 70%,#d0d2d5 70%)"></div>
  <div class="note-box" style="left:210px;top:110px;width:150px;height:205px">IT Management bedeutet für uns nicht Reaktion sondern Prävention! Damit erreichen wir eine Hochverfügbarkeit der Server und Endgeräte bei unseren Kunden. Unser Management Umfasst folgende Leistungen.</div>
  <ul class="bullets" style="left:380px;top:136px;width:230px">
    <li>Geräte-Monitoring</li>
    <li>Patchmanagement für Betriebssystem-Updates</li>
    <li>Internet Content Filter (z.B. Adult Pages, Social Networks, usw.)</li>
    <li>Automatisierte Wartungsarbeiten an Server und Clients</li>
    <li>Monatliches IT Reporting an unsere Kunden</li>
  </ul>
  <div class="footer-rule" style="left:32px;top:336px;width:450px"></div>
  <div class="footer-url" style="left:492px;top:330px">www.stage.netvora-example.de</div>
</section>

<section class="slide" style="left:183px;top:556px">
  <svg class="corner" viewBox="0 0 18 18"><polygon points="0,0 18,0 0,18" fill="#f7931e"/></svg>
  <h2 class="title" style="left:56px">Arbeitsschutz Management Software</h2>
  <div class="photo" role="img" aria-label="Software product box" style="left:20px;top:108px;width:170px;height:200px;background:linear-gradient(135deg,#f7b733,#e99a1a 60%,#d9dde2 60%)"></div>
  <div class="note-box" style="left:210px;top:108px;width:150px;height:205px;padding:0 24px">With NV Kelmar you get process, documentation and legal security quickly and easily.</div>
  <ul class="bullets" style="left:385px;top:133px;width:230px">
    <li>Gefährdungsbeurteilung</li>
    <li>Maßnahmenmanagement</li>
    <li>Unterweisung / Online-Unterweisung</li>
    <li>Gefahrstoffmanagment</li>
    <li>Unfallmanagement</li>
    <li>Controlling</li>
    <li>Auditierung</li>
  </ul>
  <div class="footer-rule" style="left:32px;top:336px;width:450px"></div>
  <div class="footer-url" style="left:492px;top:330px">www.stage.netvora-example.de</div>
</section>

<section class="slide" style="left:645px;top:556px">
  <svg class="corner" viewBox="0 0 18 18"><polygon points="0,0 18,0 0,18" fill="#f7931e"/></svg>
  <h2 class="title" style="left:56px">Unsere Preise für Service und Support</h2>
  <div class="price-col" style="left:55px"><div class="price-head">Fahrtkosten</div><p>Je gefahrener KM. Unsere Techniker fahren mit einem Service-Fahrzeug zu Ihnen welches mit allen gängigen Ersatzteilen und Produkten ausgestattet ist.</p><div class="price-pill">0,80<sup>ct</sup></div></div>
  <div class="price-col" style="left:233px"><div class="price-head">Service-Einsatz</div><p>Je angefangene 1/4 Stunde für einen Service-Techniker oder Administrator.</p><div class="price-pill">21,25<sup>€</sup></div></div>
  <div class="price-col" style="left:411px"><div class="price-head">Fernwartung</div><p>je angefangene Minute Technik-Support oder Fernwartungssitzung. Die Abrechnung erfolgt über eine monatliche Sammelrechnung der erbrachten Leistungen.</p><div class="price-pill">1,42<sup>€</sup></div></div>
  <div class="footer-url" style="left:74px;top:330px">www.stage.netvora-example.de</div>
  <div class="footer-rule" style="left:230px;top:336px;width:380px"></div>
</section>

<section class="slide" style="left:183px;top:806px">
  <svg class="corner" viewBox="0 0 18 18"><polygon points="0,0 18,0 0,18" fill="#f7931e"/></svg>
  <h2 class="title" style="left:54px">Wer sind wir?</h2>
  <div class="abs" style="left:37px;top:92px;width:330px;font-size:8px;line-height:1.3;color:var(--gray)">
    <p style="margin-bottom:8px">Wir sind seit 25 Jahren ein inhabergeführtes Familienunternehmen mit Traditionen, Werten und einem ganz tollen Team.</p>
    <p>Wir legen großen Wert auf Menschlichkeit, langjährige Partnerschaften und Arbeiten auf Augenhöhe. Wir lieben unsere Arbeit, sind für unsere Mitarbeiter da und bewegen Berge für unsere Kunden.</p>
  </div>
  <div class="abs" style="left:40px;top:200px;font-size:16px;color:var(--gray)">Zahlen und Fakten 2019</div>
  <div class="stat" style="left:10px"><div class="stat-badge">560</div><span>Kundengeräte</span></div>
  <div class="stat" style="left:103px"><div class="stat-badge">3300</div><span>Tickets</span></div>
  <div class="stat" style="left:197px"><div class="stat-badge">6500</div><span>Telefonate</span></div>
  <div class="stat" style="left:282px;width:100px"><div class="stat-badge">220K</div><span>Zeilen Sourcecode</span></div>
  <div class="footer-url" style="left:74px;top:330px">www.stage.netvora-example.de</div>
  <div class="footer-rule" style="left:200px;top:336px;width:190px"></div>
  <div class="photo" role="img" aria-label="Portrait of the two company owners" style="left:398px;top:0;width:242px;height:360px;background:linear-gradient(135deg,#c8ccd0,#8e959c)"></div>
</section>

<section class="slide" style="left:645px;top:806px">
  <div class="photo" role="img" aria-label="Hand holding a smartphone with contact icons floating above" style="left:0;top:0;width:337px;height:360px;background:linear-gradient(135deg,#dadce6,#a2a6b8)"></div>
  <svg class="corner" style="left:388px;top:112px" viewBox="0 0 18 18"><polygon points="0,0 18,0 0,18" fill="#f7931e"/></svg>
  <div class="abs" style="left:412px;top:110px;font-size:26px;color:var(--orange)">Reach us at...</div>
  <svg class="abs" style="left:392px;top:165px" width="36" height="34" viewBox="0 0 36 34"><rect x="12" y="2" width="22" height="32" fill="#f7931e"/><rect x="0" y="12" width="12" height="22" fill="#f7931e"/><g fill="#fff"><rect x="16" y="6" width="4" height="4"/><rect x="26" y="6" width="4" height="4"/><rect x="16" y="14" width="4" height="4"/><rect x="26" y="14" width="4" height="4"/><rect x="16" y="22" width="4" height="4"/><rect x="26" y="22" width="4" height="4"/><rect x="3" y="17" width="4" height="4"/><rect x="3" y="25" width="4" height="4"/></g></svg>
  <div class="abs" style="left:437px;top:162px;font-size:11px;line-height:2;color:var(--text)">NV Kelmar GmbH | Lindenpfad 8 |<br>48261 Hollbrunn</div>
  <div class="abs" style="left:412px;top:228px;width:162px;height:24px;border:1.5px solid var(--orange);border-radius:12px;font-size:10px;display:flex;align-items:center;justify-content:center;color:var(--text)">Telefon 0 71 20 - 55 81 300</div>
</section>

</div>
</body>
</html>
```